Professional and modern website for Real Estate services company

Hi there! We're looking for a responsive, highly professional and modern (in line with Latest trends) coded website for a Real Estate services company named Portalia720º (find logo attached). I will try to Explain how I picture it in my head, but feel free to step out of the script and design it as you please. The structure for the website must be as Follows: - Menu: at the top of the screen, always visible (in any page and when to scrolling down). Logo at the left hand side (clicking redirects to home), then a Services, About us, Blog and Contact and on the right hand, Estimate and Log in (just placeholder, no log in required yet). - Home: (I like https://fr.domvera.example/): a landscape picture of Madrid's skyline. Very important That at a first glance (without scrolling) you can see a box to input data of your building to get an estimate (Post code, Number of homes, Number of garages, Number of stores, Swimming pool (yes / no) Concierge (yes / no)). Should there be a small space Also for a corporate presentation video (more or less like https://www.velbrastahogares.example/ but With the estimate Request box INSTEAD OF the App - however, do not take this one as example Given I just wanted to illustrate the structure). Still in the Home, bellow the first glance, I'd like to have a brief introduction of the following pages (Services, About us, Blog and Contact). This can be in a Either "square" form (like https://fr.domvera.example/) or in a "scroll" form (like https://k7pisos.example/). - Services: we offer 3 sets of services, each of them composed by three specific services, Namely: * Administration Treasury Accounting Savings * Consulting Legal Technical Regulatory * Mediation Repairs Meetings Delinquency For the sake of structuring, each of the nine services will Have to written description composed of 3 small paragraphs of About 15 words. I Tend to like to Accompany With each of the services related icons / vectors, but feel free to design them as you want. - About us: content not yet defined, but will be a series of bullets / sections in Which We talk about prep or differentiating points. We can include the corporate video presentation here again. - Blog: just a space Where you can see to the blog entries (in Home, probably just show 3/4). - Contact: a fancy contact form, with map, address, telephone, e-mail and opening hours. Just to give it a bit more content, maybe include a catch phrase like "We're looking forward to meeting you!" or something like that. - Estimate: this is the Most Important page in the website (in Addition to the upper part of the Home page). Basically replicate the estimate for the home box, but maybe with a bit more design or extended, Given this is a single page just for that. - Log in: opens a drop-down with user and password (just placeholder, no log in required yet). Regarding colors, we still do not Have a color scheme, so anything in line With the logo is OK. Many thanks in advance, Martin

All ages and genders

Real Estate

Coded - Design and coding required

5+ page

Sans Serif

Must have
• Blank colored background

```html
<!DOCTYPE html>
<html lang="en">
<head>
<meta charset="utf-8">
<title>Portalia720º — Real Estate Services</title>
<link href="https://fonts.googleapis.com/css2?family=Open+Sans:wght@400;600;700;800&display=swap" rel="stylesheet">
<style>
:root{
  --orange:#cf6a07;
  --orange-soft:#f3dcc4;
  --ink:#1f1f1f;
  --text:#555;
  --line:#d7d7d7;
  --panel:#f1f1f1;
  --white:#fff;
  --footer:#fafafa;
}
*{box-sizing:border-box;margin:0;padding:0}
html,body{width:1200px;height:2497px;overflow:hidden}
body{font-family:"Open Sans",Arial,sans-serif;color:var(--text);background:var(--white);font-size:13px}
section,header,footer{position:relative;width:1200px}

/* header */
.site-header{height:93px;border-top:5px solid var(--orange);background:var(--white);box-shadow:0 1px 4px rgba(0,0,0,.08);z-index:2}
.brand{position:absolute;left:98px;top:22px;display:flex;align-items:center;gap:10px;font-weight:800;font-size:38px;color:var(--ink);letter-spacing:-1px}
.brand-mark{width:16px;height:16px;background:var(--orange)}
.main-nav{position:absolute;left:471px;top:32px;display:flex}
.main-nav a{display:flex;align-items:center;gap:7px;font-size:16px;font-weight:600;color:#333;text-decoration:none;margin-right:34px}
.main-nav a.active{color:var(--orange)}
.main-nav svg{width:15px;height:15px;fill:currentColor}
.login-btn{position:absolute;left:1020px;top:30px;width:80px;height:37px;border-radius:6px;background:var(--orange);color:var(--white);font-weight:600;font-size:15px;display:flex;align-items:center;justify-content:center;gap:7px}
.login-btn svg{width:12px;height:14px;fill:var(--white)}

/* hero */
.hero{height:439px}
.hero-photo{position:absolute;inset:0;background:linear-gradient(180deg,#4c7fb4 0%,#8fb2d3 28%,#9aa3a6 45%,#6f6655 70%,#4d4a3e 100%)}
.hero-title{position:absolute;left:98px;top:150px;color:var(--white);font-weight:700;font-size:74px;letter-spacing:1px;text-shadow:0 2px 6px rgba(0,0,0,.35)}
.hero-title sup{font-size:40px;font-weight:400;vertical-align:36px}
.hero-sub{position:absolute;left:98px;top:237px;color:var(--white);font-size:35px;font-weight:400;text-shadow:0 2px 6px rgba(0,0,0,.35)}
.slider-dots{position:absolute;left:541px;top:393px;display:flex;gap:8px}
.slider-dots span{width:24px;height:4px;background:rgba(255,255,255,.55)}
.slider-dots span.on{background:var(--white)}

.estimate{position:absolute;left:775px;top:20px;width:325px;height:396px;background:var(--white);border-top:4px solid var(--orange);border-radius:6px;padding:14px 19px;box-shadow:0 3px 10px rgba(0,0,0,.25)}
.estimate h2{text-align:center;font-size:21px;font-weight:600;color:var(--ink);margin-bottom:8px;line-height:29px}
.estimate label{display:block;font-size:12px;color:#666;margin-bottom:4px;line-height:17px}
.estimate .field{height:27px;border:1px solid #bbb;margin-bottom:10px}
.estimate .choice{display:flex;align-items:center;font-size:12px;color:#666;height:30px}
.estimate .choice .q{width:107px}
.estimate .choice .opt{display:flex;align-items:center;gap:3px;margin-right:9px}
.radio{width:10px;height:10px;border:1px solid #666;border-radius:50%}
.estimate-btn{margin-top:12px;height:38px;border-radius:6px;background:var(--orange);color:var(--white);font-weight:700;font-size:14px;display:flex;align-items:center;justify-content:center}

/* about */
.about{height:411px}
.about h2{position:absolute;left:98px;top:49px;font-size:32px;font-weight:600;color:var(--ink)}
.about-intro{position:absolute;left:98px;top:101px;width:480px;font-size:12px;line-height:23px}
.about-points{position:absolute;left:98px;top:166px;list-style:none}
.about-points li{display:flex;align-items:center;gap:10px;font-size:12.5px;height:35px;color:#444}
.tick{width:14px;height:14px;border-radius:50%;background:var(--orange);display:flex;align-items:center;justify-content:center}
.tick svg{width:9px;height:9px}
.btn-small{position:absolute;left:98px;top:325px;width:120px;height:33px;border-radius:6px;background:var(--orange);color:var(--white);font-weight:700;font-size:12px;display:flex;align-items:center;justify-content:center}
.video{position:absolute;left:622px;top:55px;width:476px;height:301px;border:2px solid #ddd;padding:4px;background:var(--white);box-shadow:0 1px 3px rgba(0,0,0,.12)}
.video-frame{position:relative;width:100%;height:100%;background:linear-gradient(115deg,#9bb5cd 0%,#c8d6e3 40%,#4a6b8c 70%,#2d3f57 100%)}
.video-play{position:absolute;left:212px;top:122px;width:50px;height:50px;border-radius:50%;background:rgba(20,20,20,.85);display:flex;align-items:center;justify-content:center}
.video-side{position:absolute;right:8px;width:30px;height:28px;border-radius:4px;background:rgba(20,20,20,.85)}
.video-bar{position:absolute;left:8px;right:8px;bottom:8px;height:36px;display:flex;gap:6px}
.video-bar .pb{width:58px;background:rgba(20,20,20,.88);border-radius:3px;display:flex;align-items:center;justify-content:center}
.video-bar .track{flex:1;background:rgba(20,20,20,.8);border-radius:3px;position:relative}
.video-bar .track::after{content:"";position:absolute;left:8px;right:130px;top:16px;height:5px;background:#555}

/* services */
.services{height:476px;background:var(--panel)}
.section-title{position:absolute;left:0;width:1200px;text-align:center;font-size:30px;font-weight:600;color:var(--ink)}
.services .section-title{top:34px}
.service{position:absolute;top:100px;width:340px;text-align:center}
.service .ring{width:183px;height:183px;margin:0 auto;border-radius:50%;border:1px solid #555;display:flex;align-items:center;justify-content:center}
.service .ring-inner{width:169px;height:169px;border-radius:50%;border:5px solid #444;display:flex;align-items:center;justify-content:center}
.service.featured .ring,.service.featured .ring-inner{border-color:var(--orange)}
.service-art{width:84px;height:84px;border-radius:50%;background:radial-gradient(circle,var(--orange) 0%,#de8a3a 60%,var(--orange-soft) 100%)}
.service h3{margin-top:22px;font-size:20px;font-weight:400;color:var(--ink);letter-spacing:.4px}
.service p{margin:10px auto 0;width:262px;font-size:12px;line-height:22px;color:#666}
.service .more{display:block;margin-top:14px;font-size:12px;font-weight:700;color:var(--orange)}

/* blog */
.blog{height:506px}
.blog .section-title{top:37px}
.post{position:absolute;top:97px;width:321px}
.post-photo{position:relative;height:211px;border:2px solid #ddd;padding:4px;background:var(--white)}
.post-photo .fill{width:100%;height:100%}
.date{position:absolute;left:-9px;top:136px;width:43px;height:60px;background:var(--orange);color:var(--white);text-align:center;line-height:1}
.date b{display:block;font-size:24px;font-weight:700;margin-top:6px}
.date span{font-size:12px}
.post h3{margin-top:16px;font-size:19px;font-weight:600;color:var(--ink)}
.post p{margin-top:8px;font-size:12px;line-height:21px;color:#666}
.post hr{border:none;border-top:1px solid var(--line);margin-top:20px}
.meta{display:flex;gap:18px;margin-top:18px;font-size:12px;color:#666}
.meta span{display:flex;align-items:center;gap:6px}
.meta svg{width:12px;height:12px;fill:var(--orange)}

/* contact */
.contact{height:501px;background:var(--panel)}
.contact .section-title{top:38px}
.contact h4{position:absolute;top:104px;font-size:15px;font-weight:600;color:var(--ink)}
.form-field{position:absolute;width:278px}
.form-field label{display:block;font-size:11px;color:#555;margin-bottom:6px}
.form-field .box{height:32px;background:var(--white);border:1px solid #c9c9c9}
.form-field.message{width:564px}
.form-field.message .box{height:102px}
.submit{position:absolute;left:591px;top:411px;width:71px;height:30px;border-radius:4px;background:var(--orange);color:var(--white);font-weight:700;font-size:12px;display:flex;align-items:center;justify-content:center}
.info{position:absolute;display:flex;align-items:center;gap:18px;font-size:12px;line-height:21px;color:#555}
.icon-circle{width:36px;height:36px;border-radius:50%;border:1px solid #bbb;display:flex;align-items:center;justify-content:center}
.icon-circle svg{width:16px;height:16px;fill:var(--orange)}
.map{position:absolute;left:724px;top:267px;width:376px;height:188px;border:2px solid #ddd;padding:4px;background:var(--white)}
.map .fill{width:100%;height:100%;background:linear-gradient(135deg,#e9e4d6 0%,#efe9dc 45%,#dfe6d2 100%)}

/* footer */
.site-footer{height:71px;background:var(--footer)}
.copyright{position:absolute;left:98px;top:27px;font-size:12px;color:#555}
.social{position:absolute;left:967px;top:20px;display:flex;gap:7px}
.social span{width:30px;height:30px;border-radius:50%}
</style>
</head>
<body>

<header class="site-header">
  <div class="brand"><span class="brand-mark"></span>Portalia720º</div>
  <nav class="main-nav">
    <a class="active" href="#"><svg viewBox="0 0 16 16"><path d="M8 1 0 8h2v7h4v-5h4v5h4V8h2z"/></svg>Home</a>
    <a href="#"><svg viewBox="0 0 16 16"><circle cx="6" cy="8" r="4"/><circle cx="12.5" cy="4.5" r="2.5"/><circle cx="12.5" cy="12" r="2.5"/></svg>Services</a>
    <a href="#"><svg viewBox="0 0 16 16"><circle cx="8" cy="8" r="7.5"/><rect x="7" y="7" width="2" height="5" fill="#fff"/><circle cx="8" cy="4.6" r="1.1" fill="#fff"/></svg>About us</a>
    <a href="#"><svg viewBox="0 0 16 16"><path d="M2 2h12v9H7l-4 3v-3H2z"/></svg>Blog</a>
    <a href="#"><svg viewBox="0 0 16 16"><path d="M0 3h16v10H0z"/><path d="M0 3l8 6 8-6" stroke="#fff" stroke-width="1.4" fill="none"/></svg>Contact</a>
  </nav>
  <div class="login-btn"><svg viewBox="0 0 12 14"><rect y="6" width="12" height="8" rx="1"/><path d="M3 6V4a3 3 0 0 1 6 0v2" stroke="#fff" stroke-width="1.8" fill="none"/></svg>Login</div>
</header>

<section class="hero">
  <div class="hero-photo" role="img" aria-label="Panoramic photograph of the Madrid skyline under a blue sky"></div>
  <h1 class="hero-title">PORTALIA 720<sup>0</sup></h1>
  <p class="hero-sub">We are a real estate company</p>
  <div class="slider-dots"><span></span><span></span><span class="on"></span><span></span></div>

  <form class="estimate">
    <h2>ESTIMATE</h2>
    <label>Post code</label><div class="field"></div>
    <label>Number of Homes</label><div class="field"></div>
    <label>Number of Garages</label><div class="field"></div>
    <label>Number of Stores</label><div class="field"></div>
    <div class="choice"><span class="q">Swimming pool :</span><span class="opt"><i class="radio"></i>Yes</span><span class="opt"><i class="radio"></i>No</span></div>
    <div class="choice"><span class="q">Concierge :</span><span class="opt"><i class="radio"></i>Yes</span><span class="opt"><i class="radio"></i>No</span></div>
    <div class="estimate-btn">GET AN ESTIMATE</div>
  </form>
</section>

<section class="about">
  <h2>About Portalia 720º</h2>
  <p class="about-intro">At vero eos et accusamus et iusto odio dignissimos ducimus qui blanditiis praesent ium voluptatum deleniti atque corrupti quos dolores.</p>
  <ul class="about-points">
    <li><span class="tick"><svg viewBox="0 0 10 10"><path d="M1.5 5 4 7.5 8.5 2.5" stroke="#fff" stroke-width="1.8" fill="none"/></svg></span>Nam libero tempore, cum soluta nobis est eligendi optio cum</li>
    <li><span class="tick"><svg viewBox="0 0 10 10"><path d="M1.5 5 4 7.5 8.5 2.5" stroke="#fff" stroke-width="1.8" fill="none"/></svg></span>Temporibus autem quibusdam et aut officiis debitis aut rerum necessita</li>
    <li><span class="tick"><svg viewBox="0 0 10 10"><path d="M1.5 5 4 7.5 8.5 2.5" stroke="#fff" stroke-width="1.8" fill="none"/></svg></span>At vero eos et accusamus et iusto odio dignissimos ducimus qui bland</li>
    <li><span class="tick"><svg viewBox="0 0 10 10"><path d="M1.5 5 4 7.5 8.5 2.5" stroke="#fff" stroke-width="1.8" fill="none"/></svg></span>Et harum quidem rerum facilis est et expedita distinctio</li>
  </ul>
  <div class="btn-small">READ MORE &gt;&gt;</div>

  <div class="video">
    <div class="video-frame" role="img" aria-label="Corporate presentation video still: a hand holding a model of office towers">
      <span class="video-side" style="top:8px"></span>
      <span class="video-side" style="top:42px"></span>
      <div class="video-play"><svg width="18" height="20" viewBox="0 0 18 20"><path d="M2 1 17 10 2 19z" fill="#fff"/></svg></div>
      <div class="video-bar">
        <div class="pb"><svg width="16" height="18" viewBox="0 0 16 18"><path d="M1 1 15 9 1 17z" fill="#fff"/></svg></div>
        <div class="track"></div>
      </div>
    </div>
  </div>
</section>

<section class="services">
  <h2 class="section-title">Our Services</h2>

  <article class="service" style="left:65px">
    <div class="ring"><div class="ring-inner">
      <div class="service-art" role="img" aria-label="Icon for administration services"></div>
    </div></div>
    <h3>Administration</h3>
    <p>At vero eos et accusamus et iusto odio dignis simos ducimus qui blanditiis praesentium volupta tum deleniti atque corrupti quos dolo</p>
    <span class="more">READ MORE &gt;&gt;</span>
  </article>

  <article class="service featured" style="left:429px">
    <div class="ring"><div class="ring-inner">
      <div class="service-art" role="img" aria-label="Icon for consulting services"></div>
    </div></div>
    <h3>Consulting</h3>
    <p>At vero eos et accusamus et iusto odio dignis simos ducimus qui blanditiis praesentium volupta tum deleniti atque corrupti quos dolo</p>
    <span class="more">READ MORE &gt;&gt;</span>
  </article>

  <article class="service" style="left:792px">
    <div class="ring"><div class="ring-inner">
      <div class="service-art" role="img" aria-label="Icon for mediation services"></div>
    </div></div>
    <h3>Mediation</h3>
    <p>At vero eos et accusamus et iusto odio dignis simos ducimus qui blanditiis praesentium volupta tum deleniti atque corrupti quos dolo</p>
    <span class="more">READ MORE &gt;&gt;</span>
  </article>
</section>

<section class="blog">
  <h2 class="section-title">Our Blog</h2>

  <article class="post" style="left:98px">
    <div class="post-photo">
      <div class="fill" role="img" aria-label="Businessman seen from behind looking up at glass office towers" style="background:linear-gradient(135deg,#6d8fb3 0%,#dfe9f2 45%,#7f97b0 100%)"></div>
      <div class="date"><b>01</b><span>NOV</span></div>
    </div>
    <h3>Finibus Bonorum et Malorum</h3>
    <p>Nam libero tempore, cum soluta nobis est eligendi optio cumque nihil impedit quo minus id quod maxim.</p>
    <hr>
    <div class="meta"><span><svg viewBox="0 0 12 12"><circle cx="6" cy="3.5" r="3"/><path d="M0 12c0-4 3-6 6-6s6 2 6 6z"/></svg>John Doe</span><span><svg viewBox="0 0 12 12"><path d="M1 1h10v7H5l-3 3V8H1z"/></svg>3 Comments</span></div>
  </article>

  <article class="post" style="left:441px">
    <div class="post-photo">
      <div class="fill" role="img" aria-label="Madrid business district towers at sunset" style="background:linear-gradient(180deg,#3d5f93 0%,#8aa1c4 45%,#d9a27a 75%,#6b6456 100%)"></div>
      <div class="date"><b>01</b><span>NOV</span></div>
    </div>
    <h3>Finibus Bonorum et Malorum</h3>
    <p>Nam libero tempore, cum soluta nobis est eligendi optio cumque nihil impedit quo minus id quod maxim.</p>
    <hr>
    <div class="meta"><span><svg viewBox="0 0 12 12"><circle cx="6" cy="3.5" r="3"/><path d="M0 12c0-4 3-6 6-6s6 2 6 6z"/></svg>John Doe</span><span><svg viewBox="0 0 12 12"><path d="M1 1h10v7H5l-3 3V8H1z"/></svg>3 Comments</span></div>
  </article>

  <article class="post" style="left:784px">
    <div class="post-photo">
      <div class="fill" role="img" aria-label="Estate agent showing a house for sale to a couple" style="background:linear-gradient(135deg,#a9b98e 0%,#d8cbb2 45%,#7b8c6a 100%)"></div>
      <div class="date"><b>01</b><span>NOV</span></div>
    </div>
    <h3>Finibus Bonorum et Malorum</h3>
    <p>Nam libero tempore, cum soluta nobis est eligendi optio cumque nihil impedit quo minus id quod maxim.</p>
    <hr>
    <div class="meta"><span><svg viewBox="0 0 12 12"><circle cx="6" cy="3.5" r="3"/><path d="M0 12c0-4 3-6 6-6s6 2 6 6z"/></svg>John Doe</span><span><svg viewBox="0 0 12 12"><path d="M1 1h10v7H5l-3 3V8H1z"/></svg>3 Comments</span></div>
  </article>
</section>

<section class="contact">
  <h2 class="section-title">Contact Us</h2>
  <h4 style="left:98px">Get In Touch:</h4>
  <div class="form-field" style="left:98px;top:140px"><label>NAME :</label><div class="box"></div></div>
  <div class="form-field" style="left:386px;top:140px"><label>PHONE :</label><div class="box"></div></div>
  <div class="form-field" style="left:98px;top:210px"><label>EMAIL :</label><div class="box"></div></div>
  <div class="form-field" style="left:386px;top:210px"><label>ADDRESS :</label><div class="box"></div></div>
  <div class="form-field message" style="left:98px;top:278px"><label>MESSAGE :</label><div class="box"></div></div>
  <div class="submit">SUBMIT</div>

  <h4 style="left:724px">We're looking forward to meeting you!</h4>
  <div class="info" style="left:724px;top:140px">
    <span class="icon-circle"><svg viewBox="0 0 16 16"><path d="M8 1a5 5 0 0 0-5 5c0 4 5 9 5 9s5-5 5-9a5 5 0 0 0-5-5z"/><circle cx="8" cy="6" r="2" fill="#fff"/></svg></span>
    <span>18 Calle Alderan, Suite 402<br>Madrid, Spain</span>
  </div>
  <div class="info" style="left:724px;top:204px">
    <span class="icon-circle"><svg viewBox="0 0 16 16"><path d="M4 1 6.5 5 5 6.5c1 2 2.5 3.5 4.5 4.5L11 9.5l4 2.5-1.5 3C7 15 1 9 1 2.5z"/></svg></span>
    <span>900 555 0172</span>
  </div>
  <div class="info" style="left:875px;top:204px">
    <span class="icon-circle"><svg viewBox="0 0 16 16"><path d="M1 3h14v10H1z"/><path d="M1 3l7 6 7-6" stroke="#fff" stroke-width="1.4" fill="none"/></svg></span>
    <span>info@portalia720.example</span>
  </div>
  <div class="map"><div class="fill" role="img" aria-label="Street map of Madrid with a location pin on the office"></div></div>
</section>

<footer class="site-footer">
  <p class="copyright">Copyrights © 2016, Portalia 720. All Rights Reserved.</p>
  <div class="social">
    <span style="background:#3b5a98"></span>
    <span style="background:#2fa9e0"></span>
    <span style="background:#d9332b"></span>
    <span style="background:#a0825c"></span>
  </div>
</footer>

</body>
</html>
```